Financing company needs a 1-page website with contact form

We are a financing company focusing on manufacturing sector. We need a simple 1 page website with contact form that is consistent and aligned to the main website (it is part of a bigger company). Please adhere to the same color scheme to make it look similar, but not necessarily a carbon copy.

Website link www.orvik-holdings.net

I also need the designer to suggest stock images that are suitable (related to manufacturing sector).

Files to be in html format.

Font: Try to match the main website or use a simple, sans serif font that is similar
Updates

Project Deadline Extended
Reason: Dear designers, thank you for your submissions. I believe I have given my feedback to all of you. But we would like to extend it by a few days to give a chance for more designers to join, and tweak the existing submissions. Thanks!

Target Market(s)

Small and medium companies in manufacturing sector, potential investors

Industry/Entity Type

Financial Service

Font styles to use
Sans Serif

Requirements
Must have
• Consistency to the main website www.orvik-holdings.net
• Can use simialr layout too to make it easier
• Contact form
• to have a one page website like this example https://www.trymolbe.com/

```html
<!DOCTYPE html>
<html lang="en">
<head>
<meta charset="utf-8">
<title>Orvik Arclight</title>
<link href="https://fonts.googleapis.com/css2?family=Open+Sans:wght@400;600;700&display=swap" rel="stylesheet">
<style>
:root{
  --red:#b31b29;
  --dark:#3e3e3e;
  --darker:#2c2c2c;
  --light:#ececec;
  --white:#ffffff;
  --ink:#333333;
  --muted:#666666;
  --field:#ffffff;
}
*{box-sizing:border-box;margin:0;padding:0}
html,body{width:1200px;height:900px;overflow:hidden;background:var(--white);font-family:"Open Sans",Arial,sans-serif}
.board{position:relative;width:1200px;height:900px}
.abs{position:absolute}
.center{text-align:center}

/* full page view */
.page{position:absolute;left:0;top:0;width:369px;height:900px;overflow:hidden}
.hero-photo{background:linear-gradient(180deg,#3a3a3a 0%,#4a4a4a 45%,#2e2e2e 100%)}
.brand{display:flex;align-items:center;gap:4px;color:var(--white);font-weight:400;letter-spacing:.02em}
.brand .mark{background:var(--red)}
.nav{display:flex;color:var(--white);font-weight:600}
.hero-title{color:var(--white);font-weight:600}
.scroll-btn{border:1.5px solid var(--white);border-radius:50%;display:flex;align-items:center;justify-content:center}
.band-red{background:var(--red);color:var(--white)}
.band-white{background:var(--white)}
.band-grey{background:var(--light)}
.band-dark{background:var(--dark)}
.sec-title{font-weight:400;color:var(--ink)}
.band-red .sec-title,.band-dark .sec-title{color:var(--white)}
.sec-text{color:var(--muted)}
.portrait{border-radius:50%;border:2px solid var(--white);background:radial-gradient(circle at 50% 40%,#d8c9a6,#8a7a5c 60%,#4d4436)}
.person-name{font-weight:600;color:var(--ink);font-size:5px}
.person-role{color:var(--muted);font-size:4px}
.person-bio{color:var(--muted);font-size:3.6px;line-height:1.45}
.field{background:var(--field);color:#999;font-size:4px;padding:6px 5px}
.send{background:var(--red);color:var(--white);font-size:5px;font-weight:600;display:flex;align-items:center;justify-content:center}
.office{color:var(--white);font-size:3.8px;line-height:1.6}
.office b{font-size:5px;font-weight:600;display:block;margin-bottom:2px}
.footer{background:var(--white);font-size:4px;color:var(--muted)}
.social{width:11px;height:11px;border-radius:50%;background:var(--darker)}
.legal{color:var(--red)}

/* detail view */
.zoom{position:absolute;left:370px;top:0;width:830px;height:900px;overflow:hidden}
</style>
</head>
<body>
<div class="board">

  <!-- Full page -->
  <section class="page">
    <div class="abs hero-photo" style="left:0;top:0;width:369px;height:227px" role="img" aria-label="Black and white photograph of an industrial refinery plant"></div>
    <div class="abs brand" style="left:20px;top:10px;font-size:8px"><span class="mark" style="width:5px;height:5px"></span>ORVIK ARCLIGHT</div>
    <nav class="abs nav" style="left:213px;top:11px;font-size:5px;gap:9px"><span>Who Are We</span><span>Services</span><span>Key Personnel</span><span>Contact</span></nav>
    <h1 class="abs hero-title center" style="left:20px;top:88px;width:329px;font-size:13px;line-height:21px">Nurturing Partnerships to Drive Real Economy Growth</h1>
    <div class="abs scroll-btn" style="left:174px;top:149px;width:19px;height:19px">
      <svg width="8" height="8" viewBox="0 0 10 10" fill="none" stroke="#fff" stroke-width="1.6"><path d="M2 1.5l3 3 3-3M2 5.5l3 3 3-3"/></svg>
    </div>

    <div class="abs band-red" style="left:0;top:227px;width:369px;height:90px">
      <h2 class="sec-title center" style="margin-top:28px;font-size:11px">Who Are We?</h2>
      <p class="center" style="margin:4px 22px 0;font-size:5px;line-height:1.4">Orvik Arclight Factoring is a specialist financier focusing on small and medium-sized enterprises (SMEs) in emerging markets. We provide working capital, typically in structured trade finance, to businesses in the manufacturing and retail sectors.</p>
    </div>

    <div class="abs band-white" style="left:0;top:317px;width:369px;height:101px">
      <h2 class="sec-title center" style="margin-top:28px;font-size:11px">Services</h2>
      <p class="sec-text center" style="margin:4px 26px 0;font-size:5px;line-height:1.3">Our key focus is on companies in the manufacturing sector that are in need of working capital. We meet their financing needs by developing structured offerings after a careful analysis of the companies' operations and processes. Our business model is based on structured lending in the form of trade finance facilities. How we are different is the way we combine a best practices mezzanine discipline with our experience in trade finance structuring.</p>
    </div>

    <div class="abs band-grey" style="left:0;top:418px;width:369px;height:246px">
      <h2 class="sec-title center" style="margin-top:28px;font-size:11px">Key Personnel</h2>
      <p class="sec-text center" style="margin:4px 26px 0;font-size:5px;line-height:1.3">Our team comprises of seasoned professionals from leading investment and commercial banks, trading and accounting firms. They have significant experience working in various tenures in restructuring, financing and other investments, with a proven track record in private equity and mezzanine deals, structured financing, SME credits, factoring and leasing, turnaround structuring, debt and cash collection and SME management and advisory.</p>
    </div>
    <div class="abs portrait" style="left:39px;top:502px;width:66px;height:66px" role="img" aria-label="Portrait photo of Selin Averen"></div>
    <div class="abs portrait" style="left:151px;top:502px;width:66px;height:66px" role="img" aria-label="Portrait photo of Deniz Tarlan"></div>
    <div class="abs portrait" style="left:263px;top:502px;width:66px;height:66px" role="img" aria-label="Portrait photo of Mira Colvane"></div>
    <div class="abs center" style="left:22px;top:577px;width:100px">
      <div class="person-name">Selin Averen</div><div class="person-role">Managing Partner</div>
      <p class="person-bio" style="margin-top:5px">Selin Averen's expertise spans from investment banking, especially focused on private equity, to project finance and special situations. She also has in-depth knowledge of Turkish debt and equity capital markets.</p>
    </div>
    <div class="abs center" style="left:134px;top:577px;width:100px">
      <div class="person-name">Deniz Tarlan</div><div class="person-role">Managing Partner</div>
      <p class="person-bio" style="margin-top:5px">Deniz Tarlan has significant experience in special situations, deal structuring and due diligence. Prior to Orvik Arclight Factoring, he was at a multi-strategy investment fund.</p>
    </div>
    <div class="abs center" style="left:246px;top:577px;width:100px">
      <div class="person-name">Mira Colvane</div><div class="person-role">Manager</div>
      <p class="person-bio" style="margin-top:5px">Mira Colvane is responsible for overseeing origination and portfolio management. She has close to 10 years of experience in trade finance, structured finance and commodity trading.</p>
    </div>

    <div class="abs band-dark" style="left:0;top:664px;width:369px;height:210px" role="img" aria-label="Dark background with a faint world map">
      <h2 class="sec-title center" style="margin-top:28px;font-size:11px">Contact Us</h2>
    </div>
    <div class="abs field" style="left:20px;top:710px;width:160px;height:17px">Your Name *</div>
    <div class="abs field" style="left:20px;top:735px;width:160px;height:17px">Your Email *</div>
    <div class="abs field" style="left:20px;top:760px;width:160px;height:17px">Your Phone *</div>
    <div class="abs field" style="left:189px;top:710px;width:160px;height:67px">Your Message *</div>
    <div class="abs send" style="left:156px;top:785px;width:57px;height:19px">Send Message</div>
    <div class="abs office" style="left:20px;top:818px;width:150px"><b>Turkey</b>Parkline Residence D.12, Arda Cd. No:40, Levent, Istanbul<br>Phone: +90 212 555 01 88</div>
    <div class="abs office" style="left:189px;top:818px;width:160px"><b>Hong Kong</b>Room 302, 3/F, Harbourline Tower, 8 Lantern Road, Kwai Chung, N.T., Hong Kong</div>

    <footer class="abs footer" style="left:0;top:874px;width:369px;height:26px">
      <span class="abs" style="left:50px;top:10px">Copyright © Orvik Group</span>
      <span class="abs social" style="left:163px;top:7px"></span>
      <span class="abs social" style="left:178px;top:7px"></span>
      <span class="abs social" style="left:194px;top:7px"></span>
      <span class="abs legal" style="left:270px;top:10px">Privacy Policy &nbsp; Terms of Use</span>
    </footer>
  </section>

  <!-- Detail view -->
  <section class="zoom">
    <div class="abs hero-photo" style="left:0;top:0;width:830px;height:509px" role="img" aria-label="Black and white photograph of an industrial refinery plant"></div>
    <div class="abs brand" style="left:45px;top:22px;font-size:20px;gap:8px"><span class="mark" style="width:12px;height:12px"></span>ORVIK ARCLIGHT</div>
    <nav class="abs nav" style="left:479px;top:24px;font-size:12.5px;gap:20px"><span>Who Are We</span><span>Services</span><span>Key Personnel</span><span>Contact</span></nav>
    <h1 class="abs hero-title center" style="left:40px;top:195px;width:750px;font-size:30px;line-height:49px">Nurturing Partnerships to Drive Real Economy Growth</h1>
    <div class="abs scroll-btn" style="left:392px;top:335px;width:44px;height:44px;border-width:2px">
      <svg width="18" height="18" viewBox="0 0 10 10" fill="none" stroke="#fff" stroke-width="1.3"><path d="M2 1.5l3 3 3-3M2 5.5l3 3 3-3"/></svg>
    </div>

    <div class="abs band-red" style="left:0;top:509px;width:830px;height:202px">
      <h2 class="sec-title center" style="margin-top:62px;font-size:26px">Who Are We?</h2>
      <p class="center" style="margin:6px 40px 0;font-size:12.5px;line-height:1.05">Orvik Arclight Factoring is a specialist financier focusing on small and medium-sized enterprises (SMEs) in emerging markets.<br>We provide working capital, typically in structured trade finance, to businesses in the manufacturing and retail sectors.</p>
    </div>

    <div class="abs band-white" style="left:0;top:711px;width:830px;height:189px">
      <h2 class="sec-title center" style="margin-top:62px;font-size:26px">Services</h2>
      <p class="sec-text center" style="margin:6px 50px 0;font-size:12.5px;line-height:1.1">Our key focus is on companies in the manufacturing sector that are in need of working capital. We meet their financing needs by developing structured offerings after a careful analysis of the companies' operations and processes. Our business model is based on structured lending in the form of trade finance facilities. How we are different is the way we combine a best practices mezzanine discipline with our experience in trade finance structuring.</p>
    </div>
  </section>

</div>
</body>
</html>
```